A very simple 3-4 page website, wine consluting
A comprehensive and clear design brief is included
Beverages
www.veLumaconsulting.example
see brief
left side
JPG company logo, many formats available
EPS company logo, many formats available
Website Brief
my photo, not required
For Gavin
for Gavin

```html
<!DOCTYPE html>
<html lang="en">
<head>
<meta charset="utf-8">
<title>veLuma consulting – your China wine market insider</title>
<link href="https://fonts.googleapis.com/css2?family=PT+Sans:wght@400;700&display=swap" rel="stylesheet">
<style>
  :root {
    --brand-red: #c8141c;
    --brand-red-dark: #9e0d14;
    --text-dark: #1c1c1c;
    --text-grey: #8a8a8a;
    --text-light: #a8a8a8;
    --rule: #e2e2e2;
    --panel: #ffffff;
    --bg-top: #d9d9d9;
    --bg-bottom: #ffffff;
  }
  * { box-sizing: border-box; margin: 0; padding: 0; }
  html, body { width: 1200px; height: 799px; overflow: hidden; }
  body {
    font-family: "PT Sans", Tahoma, sans-serif;
    background: linear-gradient(180deg, var(--bg-top) 0%, #f2f2f2 28%, var(--bg-bottom) 55%, #f7f7f7 100%);
    position: relative;
    color: var(--text-dark);
  }
  .brand {
    position: absolute; left: 300px; top: 40px;
    display: flex; align-items: center; gap: 14px;
  }
  .brand-dot {
    width: 34px; height: 34px; border-radius: 50%;
    background: var(--brand-red);
  }
  .brand-name {
    font-size: 58px; font-weight: 700; color: var(--brand-red);
    letter-spacing: 1px; line-height: 1;
  }
  .tagline {
    position: absolute; left: 476px; top: 152px;
    font-size: 17px; color: var(--text-grey);
  }
  .nav-band {
    position: absolute; left: 925px; top: 30px;
    width: 170px; height: 560px; border-radius: 40px;
    background: linear-gradient(90deg, var(--brand-red-dark), var(--brand-red) 45%, var(--brand-red-dark));
  }
  .main-nav {
    position: absolute; left: 970px; top: 250px;
    list-style: none;
  }
  .main-nav li { font-size: 16px; color: #fff; line-height: 35px; }
  .content-panel {
    position: absolute; left: 187px; top: 197px;
    width: 760px; height: 422px;
    background: var(--panel);
    box-shadow: 0 0 24px rgba(0,0,0,0.25);
  }
  .intro {
    position: absolute; left: 46px; top: 44px; width: 680px;
    font-size: 26px; line-height: 43px; color: var(--text-dark);
  }
  .intro strong { font-weight: 700; }
  .divider {
    position: absolute; left: 46px; right: 36px; top: 276px;
    border-top: 1px solid var(--rule);
  }
  .testimonial-quote {
    position: absolute; left: 46px; top: 296px; width: 440px;
    font-size: 12.5px; line-height: 20px; color: var(--text-light);
  }
  .testimonial-quote .mark { font-size: 22px; line-height: 0; color: var(--text-light); }
  .testimonial-source {
    position: absolute; left: 545px; top: 294px; width: 210px;
  }
  .testimonial-source h2 {
    font-size: 13px; font-weight: 400; color: var(--text-grey); margin-bottom: 18px;
  }
  .testimonial-source .person { margin-left: 20px; }
  .testimonial-source .name { font-size: 14px; color: var(--text-grey); margin-bottom: 6px; }
  .testimonial-source .role { font-size: 10px; line-height: 15px; color: var(--text-light); }
  .site-footer {
    position: absolute; left: 187px; top: 660px;
    font-size: 13px; color: var(--text-grey);
  }
  .site-footer span { position: absolute; white-space: nowrap; top: 0; }
  .footer-mark {
    position: absolute; left: 770px; top: 657px;
    font-size: 20px; color: #9a9a9a; letter-spacing: 1px;
  }
</style>
</head>
<body>
  <div class="nav-band"></div>

  <header class="brand">
    <span class="brand-dot"></span>
    <span class="brand-name">veLuma consulting</span>
  </header>
  <p class="tagline">your China wine market insider</p>

  <ul class="main-nav">
    <li>About Us</li>
    <li>Services</li>
    <li>Contact</li>
  </ul>

  <main class="content-panel">
    <p class="intro">In order to succeed in this <strong>uniquely challenging market</strong>, you need someone <strong>intimately familiar with the market</strong> who can assist you in achieving your goals. <strong>veLuma consulting</strong>, with over nine years of experience in the market, is <strong>your China wine market insider</strong>.</p>
    <div class="divider"></div>
    <blockquote class="testimonial-quote"><span class="mark">“</span>veLuma consulting's unique and extensive experience in the market provided us with pragmatic and implementable strategies and tactics to implement in the market, which will greatly assist our wine producers in accessing this opaque and challenging market.<span class="mark">”</span></blockquote>
    <aside class="testimonial-source">
      <h2>What others say about us</h2>
      <div class="person">
        <p class="name">Tomas Ferrel</p>
        <p class="role">Chief Economic and Commercial Counselor,<br>Trade and Commerce Office of Valderra (Beijing)</p>
      </div>
    </aside>
  </main>

  <footer class="site-footer">
    <span style="left:0">info@veLumaconsulting.example</span>
    <span style="left:255px">Skype: veluma.consulting</span>
    <span style="left:437px">Tel: +852 5550 0142</span>
  </footer>
  <div class="footer-mark">veLuma</div>
</body>
</html>
```